New design for a hotel booking website

I am looking to re-design my hotel booking website peakstaylodging.net. Please find the specs attached. Delivery in PSD format. Two pages total: (i) homepage and (ii) inner page.
I want the design to be very simple to navigate and have a feel that is related to Banff, Canada. You can keep a similar layout as the current website.
Requirements
1) Homepage
- Booking form above the fold containing the check in & check out dates, # of rooms and the Search button
- Quality image relating to the city of Banff to make it clear what city this is (no slider - I don't want any animation)
- A section for featured hotels (3-5 items)
- A section for links to other sections on the website (currently under "Explore Banff")
- A section for articles and local guides
- A weather widget (either in the header or somewhere else, similar to this one http://clipvanta.com/t/QX7RLPd2K4)
2) Hotel listings page - http://www.peakstaylodging.net/hotels
- Left or right sidebar – must contain the booking form with the same fields as on the homepage
- A section of why to book hotels with us under the booking form
- Each hotel listing should contain the following
Hotel name
Star rating
Short description (same as currently on the website)
Thumbnail
Address
A button to Check Rates
Notes
- I want the design to be user friendly, simple and easy to use
- I want it to be related to Banff. Banff is a resort town in Alberta, Canada with mountains for skiing in the winter and parks and wildlife nature in the summer.
- Delivery format: PSD
- I want the layout to be easily convertible into a responsive design
- Small social media icon to the Chatterly page (with the option to add Vidzo and Quippr in the future)
Some competing website examples:
1) corvelridgeway.com/Places-to-Stay/Hotels-Inns
2) tornivastays.org
Some examples of websites I liked:
1) http://www.quellmont.com/accommodation/hotels/
2) http://www.lodgevanterra.com/
Target Market(s)
Anyone looking to book their stay in Banff, AB, Canada.
Industry/Entity Type
Travel
Number of Pages Required
2 page
Look and feel

```html
<!DOCTYPE html>
<html lang="en">
<head>
<meta charset="utf-8">
<title>Peakstay Lodging – Compare Prices On Accommodations In Banff</title>
<link rel="stylesheet" href="https://fonts.googleapis.com/css2?family=Anton&family=Arimo:wght@400;700&family=Roboto+Condensed:wght@700&family=Tinos&display=swap">
<style>
:root{
  --forest:#0b4716;
  --panel-green:#9fd497;
  --ink:#111;
  --royal:#1a1ac4;
  --link-blue:#1f4fb4;
  --price-red:#c41e2a;
  --sidebar-grey:#c9c9c9;
  --card-grey:#dedede;
  --widget:#2c3440;
  --white:#fff;
}
*{box-sizing:border-box;margin:0;padding:0}
html,body{width:869px;height:1200px;overflow:hidden;background:var(--white)}
body{position:relative;font-family:"Arimo",Arial,sans-serif;color:var(--ink)}
.abs{position:absolute}

.brand{left:48px;top:14px;font-family:"Anton",Impact,sans-serif;font-size:35px;letter-spacing:.5px;color:var(--royal);line-height:1}
.tagline{left:50px;top:58px;font-family:"Tinos","Times New Roman",serif;font-size:17px;color:var(--royal)}
.weather{left:691px;top:22px;width:123px;height:52px;background:var(--widget);color:#ccc;font-size:7px;line-height:11px;padding:8px 0 0 8px}
.weather .city{padding-left:15px}
.weather .temp{color:#e8c200;font-weight:700;padding-left:42px}
.weather svg{position:absolute;right:10px;top:9px}

.main-nav{left:0;top:98px;width:869px;height:82px;background:var(--forest)}
.main-nav a{position:absolute;top:29px;font-family:"Roboto Condensed",Arial,sans-serif;font-weight:700;font-size:22px;color:var(--white);text-decoration:none}

.hero{left:51px;top:181px;width:763px;height:317px;background:linear-gradient(180deg,#8fb3d6 0%,#cfdbe6 30%,#4a5a44 48%,#e9eef2 64%,#3c4a50 100%)}
.search-panel{left:538px;top:193px;width:247px;height:294px;background:var(--panel-green);text-align:center}
.search-panel h2{font-size:17px;font-weight:700;margin-top:12px;letter-spacing:.3px}
.search-panel p{font-size:9.5px;line-height:16px;margin-top:6px}
.field{position:absolute;height:31px;border-radius:5px;background:linear-gradient(#fafafa,#d4d4d4);border:1px solid #bbb;font-weight:700;font-size:13px;text-align:left;padding:8px 0 0 22px;box-shadow:0 1px 2px rgba(0,0,0,.2)}
.field svg{position:absolute;right:12px;top:4px}
.phone{position:absolute;left:0;width:247px;top:252px;font-weight:700;font-size:17px}

.guide-photo{left:48px;top:545px;width:537px;height:179px;background:linear-gradient(180deg,#06130f 0%,#0f3a24 45%,#1e7a48 70%,#0c2218 100%)}
.guide h2{position:absolute;left:48px;top:726px;font-size:17px;font-weight:700}
.accent{color:var(--link-blue)}
.guide p{position:absolute;left:47px;width:540px;font-size:10px;line-height:12px}

.explore{left:613px;top:545px;width:196px;height:277px;background:var(--sidebar-grey)}
.explore h3{position:absolute;left:30px;top:20px;font-size:17px;font-weight:700}
.explore ul{list-style:none;position:absolute;left:10px;top:60px}
.explore li{font-size:9.5px;font-weight:700;height:24.5px;display:flex;gap:10px}
.explore li svg{margin-top:1px}

.featured-title{left:48px;top:831px;font-size:17px;font-weight:700}
.card{top:869px;width:158px;height:175px;background:var(--card-grey)}
.card .thumb{height:107px}
.card .info{padding:5px 12px;font-size:17px;line-height:21px}
.card .price{color:var(--price-red)}
.arrow{top:922px}

.site-footer{left:0;top:1077px;width:869px;height:123px;background:var(--forest);color:var(--white);text-align:center}
.social{position:absolute;left:352px;top:27px;display:flex;gap:20px}
.social span{width:20px;height:20px;border-radius:50%;background:#111;display:block}
.footer-links{position:absolute;width:100%;top:60px;font-size:13px}
.copyright{position:absolute;width:100%;top:91px;font-size:13px}
</style>
</head>
<body>

<header>
  <div class="abs brand">PEAKSTAY LODGING</div>
  <div class="abs tagline">Compare Prices On Accommodations In Banff</div>
  <div class="abs weather" aria-label="Weather: Vancouver 0°C mostly cloudy">
    <div class="city">VANCOUVER</div>
    <div class="temp">0°C</div>
    <div>MOSTLY CLOUDY</div>
    <svg width="34" height="34" viewBox="0 0 34 34"><circle cx="17" cy="17" r="15" fill="none" stroke="#fff" stroke-width="2"/><ellipse cx="17" cy="18" rx="9" ry="4" fill="#fff"/><circle cx="15" cy="15" r="4" fill="#fff"/></svg>
  </div>
</header>

<nav class="abs main-nav">
  <a style="left:59px">HOME</a>
  <a style="left:151px">BANIFF HOTELS</a>
  <a style="left:337px">BANIFF RESORTS</a>
  <a style="left:531px">LODGES</a>
  <a style="left:645px">INNS &amp; MOTELS</a>
</nav>

<div class="abs hero" role="img" aria-label="Snowy riverbank with pine trees and mountains near Banff"></div>

<form class="abs search-panel">
  <h2>SEARCH BANFF HOTELS</h2>
  <p>Enter your travel dates and find<br>available accommodations.</p>
  <div class="field" style="left:22px;top:82px;width:203px">Check-in
    <svg width="24" height="24" viewBox="0 0 24 24"><rect x="1" y="5" width="22" height="18" fill="#ccc"/><g fill="#999"><rect x="3" y="9" width="4" height="3"/><rect x="10" y="9" width="4" height="3"/><rect x="17" y="9" width="4" height="3"/><rect x="3" y="14" width="4" height="3"/><rect x="10" y="14" width="4" height="3"/><rect x="17" y="14" width="4" height="3"/><rect x="3" y="19" width="4" height="3"/><rect x="10" y="19" width="4" height="3"/><rect x="17" y="19" width="4" height="3"/></g><circle cx="7" cy="4" r="2.5" fill="#d66"/><circle cx="17" cy="4" r="2.5" fill="#d66"/></svg>
  </div>
  <div class="field" style="left:22px;top:137px;width:203px">Check-out
    <svg width="24" height="24" viewBox="0 0 24 24"><rect x="1" y="5" width="22" height="18" fill="#ccc"/><g fill="#999"><rect x="3" y="9" width="4" height="3"/><rect x="10" y="9" width="4" height="3"/><rect x="17" y="9" width="4" height="3"/><rect x="3" y="14" width="4" height="3"/><rect x="10" y="14" width="4" height="3"/><rect x="17" y="14" width="4" height="3"/><rect x="3" y="19" width="4" height="3"/><rect x="10" y="19" width="4" height="3"/><rect x="17" y="19" width="4" height="3"/></g><circle cx="7" cy="4" r="2.5" fill="#d66"/><circle cx="17" cy="4" r="2.5" fill="#d66"/></svg>
  </div>
  <div class="field" style="left:22px;top:192px;width:108px;text-align:center;padding-left:0;font-size:12px">Rooms</div>
  <div class="field" style="left:140px;top:192px;width:85px;text-align:center;padding:6px 0 0;font-size:17px">Search</div>
  <div class="phone">or call&nbsp; 1 (877) 555-0142</div>
</form>

<section class="guide">
  <div class="abs guide-photo" role="img" aria-label="Northern lights over a snowy Banff lodge at night"></div>
  <h2><span class="accent">Banff Hotel</span> Guide</h2>
  <p style="top:757px">This Banff accommodation guide is filled with useful information for anyone searching for Banff hotels,<br>Banff motels, or Banff Condos.</p>
  <p style="top:794px">Our goal is to provide a complete resource for Banff National Park hotels, and we hope you have fun finding<br>your perfect hotel in Banff Alberta Canada.</p>
</section>

<aside class="abs explore">
  <h3><span style="color:#1a1ab0">Explore</span> Banff</h3>
  <ul>
    <li><svg width="8" height="10"><path d="M1 1 L7 5 L1 9 Z" fill="none" stroke="#333"/></svg>Things to do in Banff</li>
    <li><svg width="8" height="10"><path d="M1 1 L7 5 L1 9 Z" fill="none" stroke="#333"/></svg>Banff Festivals</li>
    <li><svg width="8" height="10"><path d="M1 1 L7 5 L1 9 Z" fill="none" stroke="#333"/></svg>Experience Summit Skyride</li>
    <li><svg width="8" height="10"><path d="M1 1 L7 5 L1 9 Z" fill="none" stroke="#333"/></svg>Heli Sightseeing in Banff</li>
    <li><svg width="8" height="10"><path d="M1 1 L7 5 L1 9 Z" fill="none" stroke="#333"/></svg>Hiking in Banff</li>
    <li><svg width="8" height="10"><path d="M1 1 L7 5 L1 9 Z" fill="none" stroke="#333"/></svg>Camping &amp; Campgrounds</li>
    <li><svg width="8" height="10"><path d="M1 1 L7 5 L1 9 Z" fill="none" stroke="#333"/></svg>Hotels near Upper Hot Springs</li>
    <li><svg width="8" height="10"><path d="M1 1 L7 5 L1 9 Z" fill="none" stroke="#333"/></svg>Nearby Cities</li>
  </ul>
</aside>

<section>
  <h2 class="abs featured-title"><span class="accent">Featured</span> Hotels &amp; Accommodations</h2>
  <svg class="abs arrow" style="left:61px" width="34" height="34" viewBox="0 0 34 34"><circle cx="17" cy="17" r="17" fill="#8a8a8a"/><path d="M21 10 L11 17 L21 24 Z" fill="#fff"/></svg>
  <div class="abs card" style="left:129px"><div class="thumb" role="img" aria-label="Castle-style resort among snowy mountains" style="background:linear-gradient(180deg,#a9c6e4,#e6eef4 60%,#7d8a86)"></div><div class="info">from <span class="price">$445 CAD</span><br>Glacierpine Springs Resort</div></div>
  <div class="abs card" style="left:348px"><div class="thumb" role="img" aria-label="Resort hotel lit at dusk above snowy trees" style="background:linear-gradient(180deg,#1a3a8c,#2f5fb8 55%,#1d4aa6)"></div><div class="info">from <span class="price">$265 CAD</span><br>Stonecrest Resort Hotel</div></div>
  <div class="abs card" style="left:564px;width:155px"><div class="thumb" role="img" aria-label="Log cabin lodge surrounded by trees and gardens" style="background:linear-gradient(180deg,#9bb584,#4d6a3a 55%,#5b5b52)"></div><div class="info">from <span class="price">$256 CAD</span><br>Elkhorn Ridge Lodge</div></div>
  <svg class="abs arrow" style="left:758px" width="34" height="34" viewBox="0 0 34 34"><circle cx="17" cy="17" r="17" fill="#8a8a8a"/><path d="M13 10 L23 17 L13 24 Z" fill="#fff"/></svg>
</section>

<footer class="abs site-footer">
  <div class="social" aria-label="Social links: Chatterly, Quippr, Vidzo"><span></span><span></span><span></span><span></span></div>
  <div class="footer-links">Contacts | FAQ | Terms &amp; Conditions | Privacy Policy</div>
  <div class="copyright">Copyright © 2014 PeakstayLodging.net, All Rights Reserved.</div>
</footer>

</body>
</html>
```